Sales and Lettings Boards

Hello, please see attached our sales and lettings boards for our estate agency. These were "designed" by the sign writers. As you can see they are pretty flat and boring - could you work your magic and make them stand out please? I've also attached the logo files. Many thanks, Glen

Target Market(s)

Consumers - residential sale property sales and lettings

Industry/Entity Type

Real Estate Agent

```html
<!DOCTYPE html>
<html lang="en">
<head>
<meta charset="utf-8">
<title>NOVIS Sales &amp; Lettings – Property Boards</title>
<link rel="stylesheet" href="https://fonts.googleapis.com/css2?family=Arimo:wght@700&family=Oswald:wght@600;700&display=swap">
<style>
  :root {
    --charcoal: #555658;
    --green: #6abd45;
    --white: #ffffff;
    --frame: #e6e7e8;
    --page: #ffffff;
  }
  html, body {
    margin: 0;
    padding: 0;
    width: 1200px;
    height: 1200px;
    overflow: hidden;
    background: var(--page);
  }
  .canvas {
    position: relative;
    width: 1200px;
    height: 1200px;
    background: var(--page);
    font-family: "Arimo", Arial, sans-serif;
  }
  .presentation-frame {
    position: absolute;
    left: 40px;
    top: 40px;
    width: 1120px;
    height: 1120px;
    box-sizing: border-box;
    border: 14px solid var(--frame);
  }
  .brand-lockup {
    position: absolute;
    top: 262px;
    left: 0;
    width: 1200px;
    text-align: center;
    color: var(--charcoal);
  }
  .brand-name {
    margin: 0;
    font-size: 128px;
    line-height: 1;
    font-weight: 700;
    letter-spacing: 2px;
  }
  .brand-tagline {
    margin: 22px 0 0;
    font-size: 56px;
    line-height: 1;
    font-weight: 700;
  }
  .brand-tagline .amp { color: var(--green); }
  .board-row {
    position: absolute;
    top: 522px;
    left: 159px;
    display: flex;
    gap: 34px;
  }
  .board { display: block; width: 272px; height: 380px; }
  .board-name { font-family: "Arimo", Arial, sans-serif; font-weight: 700; font-size: 34px; fill: var(--white); }
  .board-tagline { font-family: "Arimo", Arial, sans-serif; font-weight: 700; font-size: 17px; fill: var(--white); }
  .board-tagline .amp { fill: var(--green); }
  .board-status {
    font-family: "Oswald", "Arial Narrow", sans-serif;
    font-weight: 700;
    fill: var(--charcoal);
    stroke: var(--white);
    stroke-width: 1.5px;
    paint-order: stroke;
  }
  .board-phone { font-family: "Oswald", "Arial Narrow", sans-serif; font-weight: 600; font-size: 36px; fill: var(--white); }
  .board-web { font-family: "Arimo", Arial, sans-serif; font-weight: 700; font-size: 14px; fill: var(--white); }
</style>
</head>
<body>
<main class="canvas">
  <div class="presentation-frame"></div>

  <header class="brand-lockup">
    <h1 class="brand-name">NOVIS</h1>
    <p class="brand-tagline">Sales <span class="amp">&amp;</span> Lettings</p>
  </header>

  <section class="board-row" aria-label="Property boards">
    <!-- For sale board -->
    <svg class="board" viewBox="0 0 272 380" aria-label="For sale board">
      <circle cx="136" cy="81" r="81" fill="var(--charcoal)"/>
      <rect x="0" y="49" width="272" height="331" fill="var(--charcoal)"/>
      <rect x="8" y="57" width="256" height="315" fill="none" stroke="var(--green)" stroke-width="6"/>
      <circle cx="136" cy="81" r="62" fill="var(--green)"/>
      <text class="board-name" x="136" y="188" text-anchor="middle">NOVIS</text>
      <text class="board-tagline" x="136" y="211" text-anchor="middle">Sales <tspan class="amp">&amp;</tspan> Lettings</text>
      <rect x="5" y="227" width="262" height="67" fill="var(--green)"/>
      <text class="board-status" x="136" y="279" text-anchor="middle" font-size="46" letter-spacing="2">FOR SALE</text>
      <text class="board-phone" x="136" y="334" text-anchor="middle">01632 960418</text>
      <line x1="36" y1="342" x2="236" y2="342" stroke="var(--green)" stroke-width="2"/>
      <text class="board-web" x="136" y="361" text-anchor="middle">www.novis-estates.co.uk</text>
    </svg>

    <!-- Rooms to let board -->
    <svg class="board" viewBox="0 0 272 380" aria-label="Rooms to let board">
      <circle cx="136" cy="81" r="81" fill="var(--charcoal)"/>
      <rect x="0" y="49" width="272" height="331" fill="var(--charcoal)"/>
      <rect x="8" y="57" width="256" height="315" fill="none" stroke="var(--green)" stroke-width="6"/>
      <circle cx="136" cy="81" r="62" fill="var(--green)"/>
      <text class="board-name" x="136" y="188" text-anchor="middle">NOVIS</text>
      <text class="board-tagline" x="136" y="211" text-anchor="middle">Sales <tspan class="amp">&amp;</tspan> Lettings</text>
      <rect x="5" y="227" width="262" height="67" fill="var(--green)"/>
      <text class="board-status" x="136" y="279" text-anchor="middle" font-size="42" textLength="244" lengthAdjust="spacingAndGlyphs">ROOMS TO LET</text>
      <text class="board-phone" x="136" y="334" text-anchor="middle">01632 960418</text>
      <line x1="36" y1="342" x2="236" y2="342" stroke="var(--green)" stroke-width="2"/>
      <text class="board-web" x="136" y="361" text-anchor="middle">www.novis-estates.co.uk</text>
    </svg>

    <!-- To let board -->
    <svg class="board" viewBox="0 0 272 380" aria-label="To let board">
      <circle cx="136" cy="81" r="81" fill="var(--charcoal)"/>
      <rect x="0" y="49" width="272" height="331" fill="var(--charcoal)"/>
      <rect x="8" y="57" width="256" height="315" fill="none" stroke="var(--green)" stroke-width="6"/>
      <circle cx="136" cy="81" r="62" fill="var(--green)"/>
      <text class="board-name" x="136" y="188" text-anchor="middle">NOVIS</text>
      <text class="board-tagline" x="136" y="211" text-anchor="middle">Sales <tspan class="amp">&amp;</tspan> Lettings</text>
      <rect x="5" y="227" width="262" height="67" fill="var(--green)"/>
      <text class="board-status" x="136" y="279" text-anchor="middle" font-size="46" letter-spacing="3">TO LET</text>
      <text class="board-phone" x="136" y="334" text-anchor="middle">01632 960418</text>
      <line x1="36" y1="342" x2="236" y2="342" stroke="var(--green)" stroke-width="2"/>
      <text class="board-web" x="136" y="361" text-anchor="middle">www.novis-estates.co.uk</text>
    </svg>
  </section>
</main>
</body>
</html>
```